BrookfieldVentures Business Card Design

Design business cards with attached ideas. I am open to several different ideas that would be interesting and innovative. What I have provided is logo and colors. Font should be Helvetica although it could be bold or light as needed. The design can be vertical or horizontal. The design should be more interesting than a standard business card. Files must be ready to send to a printer and in Illustrator format. The text with the five icons should be exact. Send me some ideas and I will get back to you right away. I need to choose a design within 3-5 days.

Target Market(s)

Business audience

Industry/Entity Type

Business

Contact Information for Business Card

Files should be ready to send to printer in illustrator format

Font styles to use
Sans Serif

Colors
3276b5

Requirements
Must have
• Use attached logo and two colors - blue / gray
• Include 5 offering icons and text on back
Nice to have
• Interesting and innovative design. Vertical or horizontal are both fine.

```html
<!DOCTYPE html>
<html lang="en">
<head>
<meta charset="utf-8">
<title>BrookfieldVentures Business Card</title>
<link rel="stylesheet" href="https://fonts.googleapis.com/css2?family=Arimo:wght@400&family=Source+Sans+3:wght@400;600&display=swap">
<style>
  :root {
    --stage: #000000;
    --card: #323438;
    --brand-blue: #3276b5;
    --brand-gray: #b9bcc1;
    --mark-gray: #5b5e64;
    --text-light: #f2f2f2;
  }
  * { margin: 0; padding: 0; box-sizing: border-box; }
  html, body { width: 1200px; height: 900px; overflow: hidden; background: var(--stage); }
  body { position: relative; font-family: "Source Sans 3", "Helvetica Neue", Arial, sans-serif; }

  .card {
    position: absolute;
    top: 271px;
    width: 457px;
    height: 281px;
    border-radius: 14px;
    background: radial-gradient(ellipse at 50% 40%, #37393d 0%, var(--card) 60%, #2c2e32 100%);
  }
  .card--front { left: 137px; }
  .card--back { left: 626px; }

  .brand-mark {
    position: absolute;
    background: var(--brand-blue);
    border-radius: 4px;
  }
  .card--front .brand-mark { left: 49px; top: 31px; width: 73px; height: 73px; }
  .card--back .brand-mark { left: 40px; top: 21px; width: 68px; height: 68px; }

  .brand-name {
    position: absolute;
    font-family: "Arimo", Helvetica, Arial, sans-serif;
    font-weight: 400;
    color: var(--brand-gray);
    white-space: nowrap;
    letter-spacing: -0.3px;
  }
  .card--front .brand-name { left: 136px; top: 35px; font-size: 31px; }
  .card--back .brand-name { left: 121px; top: 25px; font-size: 29px; }

  .tagline {
    position: absolute;
    font-family: "Arimo", Helvetica, Arial, sans-serif;
    color: var(--text-light);
    white-space: nowrap;
  }
  .card--front .tagline { left: 146px; top: 71px; font-size: 15px; }
  .card--back .tagline { left: 131px; top: 59px; font-size: 14px; }

  .person { position: absolute; left: 137px; top: 118px; }
  .person__name { color: var(--brand-blue); font-size: 17px; font-weight: 600; line-height: 1; }
  .person__name small { font-size: 12px; font-weight: 600; }
  .person__title { color: var(--text-light); font-size: 13px; margin-top: 3px; }

  .contact-list { position: absolute; left: 136px; top: 176px; list-style: none; }
  .contact-list li {
    display: flex; align-items: center; gap: 5px;
    color: var(--text-light); font-size: 13px; height: 19px;
  }
  .contact-list svg { width: 10px; height: 10px; fill: var(--brand-blue); }

  .offerings { position: absolute; left: 119px; top: 104px; }
  .offerings__heading { color: var(--brand-gray); font-size: 16px; font-weight: 600; margin-bottom: 13px; }
  .offerings__heading span { color: var(--brand-blue); }
  .offering-list { list-style: none; }
  .offering-list li {
    display: flex; align-items: center; gap: 9px;
    height: 25.5px; font-size: 13px; font-weight: 600; color: var(--text-light); white-space: nowrap;
  }
  .offering-list .label { color: var(--brand-blue); font-weight: 400; }
  .offering-icon { width: 18px; height: 18px; flex: none; }
</style>
</head>
<body>

<section class="card card--front" aria-label="Business card front">
  <div class="brand-mark"></div>
  <div class="brand-name">BrookfieldVentures</div>
  <div class="tagline">Twice the Value - Half the Cost</div>

  <div class="person">
    <div class="person__name">Dana Holt, <small>PhD</small></div>
    <div class="person__title">Managing Director</div>
  </div>

  <ul class="contact-list">
    <li><svg viewBox="0 0 10 10"><path d="M2 0.5l2 2-1 1.2c.6 1.3 1.6 2.3 2.9 2.9l1.2-1 2 2-1.2 1.6C4.6 9 1 5.4 0.6 1.6z"/></svg>615-555-0142</li>
    <li><svg viewBox="0 0 10 10"><path d="M0 2h10v6H0z"/><path d="M0 2l5 3.5L10 2" stroke="#323438" stroke-width="1" fill="none"/></svg>Dana@BrookfieldVentures.com</li>
    <li><svg viewBox="0 0 10 10"><circle cx="5" cy="5" r="5"/></svg>www.BrookfieldVentures.com</li>
  </ul>
</section>

<section class="card card--back" aria-label="Business card back">
  <div class="brand-mark"></div>
  <div class="brand-name">BrookfieldVentures</div>
  <div class="tagline">Twice the Value - Half the Cost</div>

  <div class="offerings">
    <h2 class="offerings__heading"><span>BrookfieldVentures</span> Offerings</h2>
    <ul class="offering-list">
      <li>
        <svg class="offering-icon" viewBox="0 0 18 18"><rect width="18" height="18" rx="2" fill="#3276b5"/><rect x="5" y="4" width="8" height="10" fill="#fff"/><path d="M6.5 7h5M6.5 9h5M6.5 11h3" stroke="#3276b5" stroke-width="0.8"/></svg>
        <span><span class="label">Concepts:</span> Thought leadership white papers</span>
      </li>
      <li>
        <svg class="offering-icon" viewBox="0 0 18 18"><rect width="18" height="18" rx="2" fill="#3276b5"/><circle cx="9" cy="6.5" r="2" fill="#fff"/><path d="M5 13.5c0-3 8-3 8 0z" fill="#fff"/><rect x="4" y="13.5" width="10" height="1.2" fill="#fff"/></svg>
        <span><span class="label">Curriculum:</span> Short courses on strategy</span>
      </li>
      <li>
        <svg class="offering-icon" viewBox="0 0 18 18"><rect width="18" height="18" rx="2" fill="#3276b5"/><circle cx="5.5" cy="6" r="1.6" fill="#fff"/><circle cx="12.5" cy="6" r="1.6" fill="#fff"/><rect x="4" y="8" width="3" height="6" fill="#fff"/><rect x="11" y="8" width="3" height="6" fill="#fff"/><path d="M8 9h2M8 11h2" stroke="#fff" stroke-width="0.8"/></svg>
        <span><span class="label">Coaching:</span> Building your strategic leadership</span>
      </li>
      <li>
        <svg class="offering-icon" viewBox="0 0 18 18"><rect width="18" height="18" rx="2" fill="#3276b5"/><path d="M9 4v4M5 12l4-4 4 4" stroke="#fff" stroke-width="0.9" fill="none"/><circle cx="9" cy="4.5" r="1.5" fill="#fff"/><circle cx="5" cy="12.5" r="1.5" fill="#fff"/><circle cx="13" cy="12.5" r="1.5" fill="#fff"/></svg>
        <span><span class="label">Consulting:</span> Developing your strategic future</span>
      </li>
      <li>
        <svg class="offering-icon" viewBox="0 0 18 18"><rect width="18" height="18" rx="2" fill="#3276b5"/><rect x="7" y="4.5" width="8" height="6" fill="none" stroke="#fff" stroke-width="0.9"/><circle cx="4.5" cy="7" r="1.3" fill="#fff"/><rect x="3.2" y="8.8" width="2.6" height="5" fill="#fff"/></svg>
        <span><span class="label">ScoreCard:</span> Balanced Scorecard and software</span>
      </li>
    </ul>
  </div>
</section>

</body>
</html>
```